TalkWell needs a Letterhead

We need a letterhead for our company "TalkWell Consultants". Logo is attached. The company color is Turquoise. Icons for website, scan logo for website, icons for address, e-mail and phone appreciated rather than just words.

```html
<!DOCTYPE html>
<html lang="en">
<head>
<meta charset="utf-8">
<title>TalkWell Consultants Letterhead</title>
<link href="https://fonts.googleapis.com/css2?family=Jost:wght@400;500&display=swap" rel="stylesheet">
<style>
  :root {
    --turquoise: #33dbe0;
    --lime: #aef000;
    --ink: #1c1c1c;
    --mark-faint: #e6f0f9;
    --paper: #ffffff;
  }
  html, body {
    margin: 0;
    padding: 0;
    overflow: hidden;
    background: var(--paper);
  }
  .letterhead {
    position: relative;
    width: 849px;
    height: 1200px;
    overflow: hidden;
    background: var(--paper);
    font-family: "Jost", sans-serif;
    color: var(--ink);
  }
  .brand {
    position: absolute;
    left: 27px;
    top: 50px;
    display: flex;
    align-items: center;
    gap: 14px;
  }
  .brand-square {
    width: 46px;
    height: 46px;
    background: var(--turquoise);
  }
  .brand-name {
    font-size: 29px;
    font-weight: 500;
    color: var(--turquoise);
    letter-spacing: 0.2px;
    line-height: 1;
  }
  .contact-list {
    position: absolute;
    right: 26px;
    top: 24px;
    margin: 0;
    padding: 0;
    list-style: none;
    text-align: right;
  }
  .contact-item {
    display: flex;
    justify-content: flex-end;
    align-items: center;
    gap: 14px;
    height: 29px;
    font-size: 17px;
    letter-spacing: 0.3px;
  }
  .contact-icon {
    width: 15px;
    height: 15px;
    flex: none;
    fill: var(--turquoise);
  }
  .watermark {
    position: absolute;
    left: 0;
    right: 0;
    top: 560px;
    text-align: center;
    font-size: 150px;
    font-weight: 500;
    color: var(--mark-faint);
    line-height: 1;
  }
  .footer-bar {
    position: absolute;
    top: 1156px;
    height: 18px;
    background: var(--lime);
  }
  .footer-bar--left { left: 0; width: 252px; }
  .footer-bar--right { left: 810px; width: 39px; }
  .address {
    position: absolute;
    left: 268px;
    top: 1153px;
    display: flex;
    align-items: center;
    gap: 14px;
    font-size: 18px;
    letter-spacing: 0.2px;
  }
  .address-icon { width: 13px; height: 18px; fill: var(--lime); }
</style>
</head>
<body>
<main class="letterhead">
  <header>
    <div class="brand">
      <span class="brand-square"></span>
      <span class="brand-name">TalkWell Consultants</span>
    </div>
    <ul class="contact-list">
      <li class="contact-item">+91 9812345670
        <svg class="contact-icon" viewBox="0 0 24 24"><path d="M6.6 10.8a15.2 15.2 0 0 0 6.6 6.6l2.2-2.2c.3-.3.7-.4 1-.2 1.1.4 2.3.6 3.6.6.6 0 1 .4 1 1V20c0 .6-.4 1-1 1A17 17 0 0 1 3 4c0-.6.4-1 1-1h3.5c.6 0 1 .4 1 1 0 1.3.2 2.5.6 3.6.1.3 0 .7-.2 1z"/></svg>
      </li>
      <li class="contact-item">+91 22 2468135
        <svg class="contact-icon" viewBox="0 0 24 24"><path d="M5 2h8v5H5zM3 8h18v14H3zm4 4v2h2v-2zm4 0v2h2v-2zm4 0v2h2v-2zm-8 4v2h2v-2zm4 0v2h2v-2zm4 0v2h2v-2z"/></svg>
      </li>
      <li class="contact-item">talkwell@mailbox.com
        <svg class="contact-icon" viewBox="0 0 24 24"><path d="M2 5h20v14H2zm2 2v.4l8 5.4 8-5.4V7zm0 2.8V17h16V9.8l-8 5.4z"/></svg>
      </li>
      <li class="contact-item">www.talkwell.com
        <svg class="contact-icon" viewBox="0 0 24 24"><path d="M12 2a10 10 0 1 0 0 20 10 10 0 0 0 0-20zm-1 2.1V8H7.6A8 8 0 0 1 11 4.1zm2 0A8 8 0 0 1 16.4 8H13zM5.5 10H11v4H5.5a8 8 0 0 1 0-4zm7.5 0h5.5a8 8 0 0 1 0 4H13zm-5.4 6H11v3.9A8 8 0 0 1 7.6 16zm5.4 0h3.4a8 8 0 0 1-3.4 3.9z"/></svg>
      </li>
    </ul>
  </header>

  <div class="watermark" aria-hidden="true">TalkWell</div>

  <footer>
    <span class="footer-bar footer-bar--left"></span>
    <div class="address">
      <svg class="address-icon" viewBox="0 0 14 20"><path d="M7 0a7 7 0 0 0-7 7c0 5 7 13 7 13s7-8 7-13a7 7 0 0 0-7-7zm0 9.5A2.5 2.5 0 1 1 7 4.5a2.5 2.5 0 0 1 0 5z"/></svg>
      <span>No.4/2, K 8th St, Bangalore, Bangalore, Karnataka - 560001.</span>
    </div>
    <span class="footer-bar footer-bar--right"></span>
  </footer>
</main>
</body>
</html>
```